Lawn maintenance
We are your green choice!
weekly , biweekly

Target Market(s)

lawn care

Industry/Entity Type

Lawn Care

Contact Information for Business Card

eye catching - not you normal "lawn business" card

Logo Text

Tall Oak Lawncare

Font styles to use
Serif
Sans Serif

Colors
ec1f27
00a990
9bcb3c
0455a3

Requirements
Must have
• Milo Hanford
• 410-555-0187
• Lawn maintenance
• We are your green choice!
• Call for a quote today!
• weekly or biweekly
Nice to have
• maybe some poker chips or playing cards
Should not have
• snow removal

```html
<!DOCTYPE html>
<html lang="en">
<head>
<meta charset="utf-8">
<title>Tall Oak Lawncare – Business Card</title>
<link href="https://fonts.googleapis.com/css2?family=Roboto:wght@400;500&display=swap" rel="stylesheet">
<style>
  :root {
    --backdrop: #262626;
    --card: #f7f7f7;
    --brand-green: #1f7a0c;
    --ink: #111111;
    --muted: #555555;
    --rule: #bdbdbd;
  }
  html, body {
    margin: 0;
    padding: 0;
    width: 1200px;
    height: 960px;
    overflow: hidden;
    background: var(--backdrop);
    font-family: "Roboto", Arial, sans-serif;
  }
  .canvas {
    position: relative;
    width: 1200px;
    height: 960px;
  }
  .business-card {
    position: absolute;
    left: 298px;
    top: 303px;
    width: 602px;
    height: 348px;
    background: var(--card);
  }
  .brand {
    position: absolute;
    left: 84px;
    top: 152px;
    display: flex;
    align-items: center;
    gap: 10px;
  }
  .brand-dot {
    width: 16px;
    height: 16px;
    border-radius: 50%;
    background: var(--brand-green);
  }
  .brand-name {
    font-size: 27px;
    font-weight: 500;
    color: var(--brand-green);
    letter-spacing: 0.5px;
    white-space: nowrap;
  }
  .divider {
    position: absolute;
    left: 345px;
    top: 110px;
    width: 1px;
    height: 136px;
    background: var(--rule);
  }
  .contact {
    position: absolute;
    left: 374px;
    top: 113px;
  }
  .contact-name {
    margin: 0;
    font-size: 24px;
    font-weight: 500;
    color: var(--brand-green);
    line-height: 30px;
  }
  .contact-phone {
    margin: 0;
    font-size: 19px;
    color: var(--ink);
    line-height: 24px;
  }
  .service-title {
    margin: 14px 0 2px;
    font-size: 14px;
    font-weight: 500;
    color: var(--brand-green);
    line-height: 18px;
  }
  .service-list {
    margin: 0;
    padding: 0;
    list-style: none;
  }
  .service-list li {
    font-size: 13px;
    color: var(--muted);
    line-height: 16.5px;
    padding-left: 14px;
    position: relative;
  }
  .service-list li::before {
    content: "";
    position: absolute;
    left: 2px;
    top: 6px;
    width: 5px;
    height: 5px;
    border-radius: 50%;
    background: var(--brand-green);
  }
</style>
</head>
<body>
  <div class="canvas">
    <div class="business-card">
      <div class="brand">
        <span class="brand-dot"></span>
        <span class="brand-name">Tall Oak Lawncare</span>
      </div>
      <div class="divider"></div>
      <div class="contact">
        <p class="contact-name">MILO HANFORD</p>
        <p class="contact-phone">410-555-0187</p>
        <p class="service-title">LAWN MAINTENANCE</p>
        <ul class="service-list">
          <li>We are your green choice!</li>
          <li>Call for a quote today!</li>
          <li>weekly or biweekly</li>
        </ul>
      </div>
    </div>
  </div>
</body>
</html>
```